Biz Cards to match new logo

I'm looking for a business card layout to go with my new logo. I'd like to have one side in colour (purple, with the logo in white) and the other side to be white with the purple logo and contact info in black font: name, address (2 lines), phone, email, fax, website. The logo includes the company name so it doesn't need to be repeated in the text. The font should be legibile to the semi-blind. (I hate small fonts on business cards).

```html
<!DOCTYPE html>
<html lang="en">
<head>
<meta charset="utf-8">
<title>Corvid Analytics – Business Card</title>
<link href="https://fonts.googleapis.com/css2?family=Arimo:wght@400;600&display=swap" rel="stylesheet">
<style>
  :root {
    --purple: #5b45b0;
    --purple-text: #4f3aa6;
    --white: #ffffff;
    --ink: #1c1c1c;
    --rule: #3a3a3a;
    --backdrop: #e6e6e8;
  }
  * { box-sizing: border-box; margin: 0; padding: 0; }
  html, body {
    width: 1200px;
    height: 900px;
    overflow: hidden;
  }
  body {
    background: var(--backdrop);
    font-family: "Arimo", Arial, sans-serif;
    display: flex;
    align-items: center;
    justify-content: center;
    gap: 40px;
  }
  .card {
    width: 540px;
    height: 310px;
    border-radius: 28px;
    position: relative;
    box-shadow: 0 6px 18px rgba(0,0,0,0.12);
    overflow: hidden;
  }
  .card-front {
    background: var(--purple);
    display: flex;
    align-items: center;
    justify-content: center;
  }
  .wordmark {
    display: flex;
    flex-direction: column;
    align-items: center;
    gap: 8px;
    font-weight: 600;
    text-transform: uppercase;
    text-align: center;
  }
  .wordmark-square {
    width: 34px;
    height: 34px;
  }
  .wordmark-name {
    letter-spacing: 0.12em;
    line-height: 1.15;
  }
  .card-front .wordmark { color: var(--white); }
  .card-front .wordmark-square { background: var(--white); }
  .card-front .wordmark-name { font-size: 34px; }

  .card-back {
    background: var(--white);
    display: flex;
    align-items: center;
  }
  .card-back .brand-area {
    width: 240px;
    display: flex;
    justify-content: center;
  }
  .card-back .wordmark { color: var(--purple-text); }
  .card-back .wordmark-square { background: var(--purple-text); width: 26px; height: 26px; }
  .card-back .wordmark-name { font-size: 22px; }
  .divider {
    width: 1px;
    height: 200px;
    background: var(--rule);
  }
  .contact {
    padding-left: 22px;
    color: var(--ink);
    font-size: 15px;
    line-height: 1.3;
  }
  .contact-name {
    color: var(--purple-text);
    font-size: 22px;
    font-weight: 400;
    letter-spacing: 0.02em;
    margin-bottom: 14px;
  }
  .contact-address { margin-bottom: 16px; }
  .contact-lines { list-style: none; }
  .label { color: var(--purple-text); }
  .website { color: var(--purple-text); }
</style>
</head>
<body>
  <section class="card card-front" aria-label="Card front">
    <div class="wordmark">
      <span class="wordmark-square" aria-hidden="true"></span>
      <span class="wordmark-name">Corvid<br>Analytics</span>
    </div>
  </section>

  <section class="card card-back" aria-label="Card back">
    <div class="brand-area">
      <div class="wordmark">
        <span class="wordmark-square" aria-hidden="true"></span>
        <span class="wordmark-name">Corvid<br>Analytics</span>
      </div>
    </div>
    <div class="divider" aria-hidden="true"></div>
    <div class="contact">
      <h1 class="contact-name">MARA ELLISON</h1>
      <p class="contact-address">Sample Road 18th Avenue,<br>Suite 400</p>
      <ul class="contact-lines">
        <li><span class="label">P:</span> +0.000.555.0100</li>
        <li><span class="label">F:</span> +0.55.777.0002</li>
        <li><span class="label">E:</span> ellison@corvidanalytics.com</li>
        <li class="website">www.corvidanalytics.com</li>
      </ul>
    </div>
  </section>
</body>
</html>
```